Insert sheet for our Dog Food Package

We need an information sheet to go inn our pet food package, with branding, and information on ingredients, nutrition and feeding guidance. We will also need two additional items which will be a variation on the label design:
1) Label for package (detailed label about us and our food)
2) Label for outer shipping box (simple label for branding)
We will start with the information, insert page. The winning designer will then deliver the package and box labels as simplified versions of the same graphical theme.
I have attached samples of an earlier drafts of the insert piece. Please disregard the style, form and colors of the examples given. THEY ARE ONLY THERE TO SHOW WHAT INFORMATION SHOULD BE INCLUDED. All colors and style should be from our logo (attached). All graphics, font styles, and placement of elements need to be YOUR creative design - not a copy of the sample we gave. PLEASE READ THIS AND PLEASE DO NOT SUBMIT ANY VARIATION OF THE EXAMPLES!!!!!!!

Target Market(s)

Pet Owners

Industry/Entity Type

Pet Food

Colors
EB3D1F
EC4F4E
F09395
F8D3D4
FCEDEE

Requirements
Must have
• All new design. New colors (based in the palette of our logo), new graphics, new fonts, new placement of elements.
Should not have
• Please disregard the style, form and colors of the examples given. THEY ARE ONLY THERE TO SHOW WHAT INFORMATION SHOULD BE INCLUDED.

```html
<!DOCTYPE html>
<html lang="en">
<head>
<meta charset="utf-8">
<title>Prepared with love for Shadow – Insert Sheet</title>
<link rel="stylesheet" href="https://fonts.googleapis.com/css2?family=Arimo:wght@400;700&family=Archivo+Black&display=swap">
<style>
  :root {
    --red: #b0252a;
    --brown: #4a1c12;
    --blush: #fcedee;
    --ink: #111111;
    --white: #ffffff;
  }
  * { margin: 0; padding: 0; box-sizing: border-box; }
  html, body { width: 966px; height: 1200px; overflow: hidden; background: var(--white); }
  .sheet {
    position: relative; width: 966px; height: 1200px; overflow: hidden;
    font-family: "Arimo", Arial, sans-serif; color: var(--ink);
  }
  .sheet-title {
    position: absolute; top: 58px; left: 0; width: 100%;
    text-align: center; font-weight: 400; font-size: 27px; letter-spacing: 0.5px;
  }
  .column { position: absolute; top: 130px; }
  .column--nutrition { left: 0; width: 403px; }
  .column--feeding { left: 561px; width: 405px; }
  .column-heading {
    font-weight: 700; font-size: 18px; text-align: center; padding-bottom: 6px;
    border-bottom: 7px solid var(--red);
  }
  .column--nutrition .column-heading { padding-left: 40px; }
  .column--feeding .column-heading { padding-right: 30px; }
  .sub-heading {
    font-size: 18px; font-weight: 400; margin-top: 14px;
  }
  .column--nutrition .sub-heading { text-align: center; padding-left: 40px; }
  .column--feeding .sub-heading { padding-left: 43px; }
  .analysis {
    display: grid; grid-template-columns: 195px 160px; margin: 12px 0 0 80px;
    font-size: 15px; row-gap: 6px;
  }
  .ingredients {
    margin: 26px 0 0 72px; width: 310px; text-align: center;
    font-size: 14.5px; line-height: 21.6px;
  }
  .feeding-table {
    margin: 14px 0 0 33px; border-collapse: collapse; font-size: 14.5px; width: 300px;
  }
  .feeding-table th { font-weight: 400; text-align: left; padding-bottom: 6px; }
  .feeding-table td { padding: 2px 0; border-bottom: 1px solid #777; line-height: 17px; }
  .feeding-table td:last-child, .feeding-table th:last-child { width: 95px; }
  .feeding-table tr:last-child td { border-bottom: 0; }
  .backdrop { position: absolute; left: 0; top: 0; }
  .story { position: absolute; left: 55px; top: 935px; width: 880px; }
  .story-title { font-family: "Archivo Black", "Arial Black", sans-serif; font-size: 50px; line-height: 1.1; color: var(--ink); }
  .story-lead { font-weight: 700; font-size: 18px; line-height: 25px; margin-top: 16px; }
  .story-quote { font-size: 16.5px; line-height: 24px; margin-top: 30px; width: 850px; }
</style>
</head>
<body>
<main class="sheet">
  <svg class="backdrop" width="966" height="1200" viewBox="0 0 966 1200">
    <path d="M0,852 C140,760 330,760 470,860 C520,895 560,890 590,850 C660,740 820,720 966,990 L966,1200 L0,1200 Z" fill="var(--blush)"/>
    <path d="M0,852 C140,760 330,760 470,860 C520,895 560,890 590,850 C660,740 820,720 966,990" fill="none" stroke="var(--red)" stroke-width="36"/>
    <path d="M250,810 C340,800 410,830 480,882 C520,910 560,912 590,885" fill="none" stroke="var(--brown)" stroke-width="6"/>
    <circle cx="194" cy="755" r="123" fill="var(--brown)"/>
    <circle cx="194" cy="755" r="108" fill="var(--white)"/>
    <circle cx="194" cy="755" r="100" fill="var(--red)" role="img" aria-label="Brand emblem illustration of an adult dog and a playful puppy"/>
  </svg>

  <h1 class="sheet-title">PREPARED WITH LOVE FOR SHADOW</h1>

  <section class="column column--nutrition">
    <h2 class="column-heading">We prepared the best for Shadow</h2>
    <h3 class="sub-heading">NUTRITION INFORMATION</h3>
    <div class="analysis">
      <span>Protein: 15%</span><span>Total fat: 9.5%</span>
      <span>Crude Fiber: 2.0%</span><span>Moisture: 72%</span>
    </div>
    <p class="ingredients">Patassium Citrate, DiCalcium Phosphate, Calcium Carbonate, Garbanzo Beans, Choline Bitartrate, Taurine, Salt, Zinc Proteinate, Magnesium Oxide, Iron Proteinate, Vitamin B-12, Selenium, Niacin, Riboflavin, Calcium Panthothenate, Thiamine, Vitamin A, Vitamin D, Calcium Iodate, Vitamin B6, Folic Acid</p>
  </section>

  <section class="column column--feeding">
    <h2 class="column-heading">How much should I feed Shadow?</h2>
    <h3 class="sub-heading">RECOMMENDED FEEDING PLAN</h3>
    <table class="feeding-table">
      <thead><tr><th>APPROXIMATE WEIGHT</th><th>FULL MEAL</th></tr></thead>
      <tbody>
        <tr><td>&lt;20lbs</td><td>110 g</td></tr>
        <tr><td>20-29 lbs</td><td>200 g</td></tr>
        <tr><td>30-39 lbs</td><td>250 g</td></tr>
        <tr><td>40-54 lbs</td><td>300 g</td></tr>
        <tr><td>55-69 lbs</td><td>350 g</td></tr>
        <tr><td>70-85 lbs</td><td>400 g</td></tr>
        <tr><td>85+ lbs</td><td>500 g</td></tr>
      </tbody>
    </table>
  </section>

  <section class="story">
    <h2 class="story-title">Our story</h2>
    <p class="story-lead">We Revolutionized the industry. Not Formulated to meet a minimum standard, but to develop the maximum health of the whole dog.</p>
    <p class="story-quote">“We didn’t just set about to create a food that will ‘pass a minimum standard’. We set out to revolutionize the industry by creating a food that is designed with Superfoods, Wholesoe Grains and Powerful Oils to help your dog achieve their maximum health, happines and longevity.</p>
  </section>
</main>
</body>
</html>
```